Harbour Fellows - community/social/support group for men needs a flyer

We need a flyer for our community group for display in GP clinics and other community services offices. Please refer to our website for design ideas: www.harbourfellows.org.au. We need it to be clean and simple to read.

Target Market(s)

Men 18+

Font styles to use
Serif

Colors
00a990

```html
<!DOCTYPE html>
<html lang="en">
<head>
<meta charset="utf-8">
<title>Harbour Fellows – Community Flyer</title>
<link rel="stylesheet" href="https://fonts.googleapis.com/css2?family=PT+Serif:ital,wght@0,400;0,700;1,400&display=swap">
<style>
  :root {
    --ink: #141414;
    --night: #0b0b26;
    --teal: #00a990;
    --teal-deep: #00705f;
    --social-box: #0a8a76;
    --white: #ffffff;
    --body-text: #1c1c1c;
  }
  * { margin: 0; padding: 0; box-sizing: border-box; }
  html, body { width: 1000px; height: 1200px; overflow: hidden; background: var(--white); }
  .flyer {
    position: relative; width: 1000px; height: 1200px; overflow: hidden;
    font-family: "PT Serif", Georgia, serif; background: var(--white);
  }
  .hero-photo {
    position: absolute; left: 0; top: 52px; width: 1000px; height: 593px;
    background:
      linear-gradient(180deg, rgba(40,10,50,0) 45%, rgba(45,15,60,0.75) 78%, rgba(25,8,40,0.95) 100%),
      radial-gradient(ellipse at 20% 30%, #e9e4d6 0%, rgba(233,228,214,0) 30%),
      linear-gradient(100deg, #8a6a5c 0%, #3f6b34 30%, #4f7a3a 55%, #2f5a2a 75%, #7a3a44 100%);
  }
  .header-art { position: absolute; left: 0; top: 0; width: 1000px; height: 130px; }
  .brand-name {
    position: absolute; left: 0; width: 485px; top: 62px; text-align: center;
    color: var(--white); font-weight: 700; font-size: 22px; letter-spacing: 1.5px; line-height: 28px;
  }
  .headline {
    position: absolute; left: 0; width: 1000px; top: 480px; text-align: center;
    color: var(--white); font-weight: 700; font-size: 44px; line-height: 54px; white-space: nowrap;
  }
  .headline-rule { position: absolute; left: 378px; top: 548px; width: 244px; height: 4px; background: var(--white); border-radius: 2px; }
  .projects-panel { position: absolute; left: 506px; top: 577px; width: 494px; height: 623px; background: var(--night); }
  .about {
    position: absolute; left: 40px; top: 684px; width: 450px;
    font-size: 18.5px; line-height: 24.8px; color: var(--body-text); white-space: nowrap;
  }
  .about strong { font-weight: 700; }
  .divider-strip { position: absolute; left: 0; top: 1054px; width: 350px; height: 10px; }
  .visit-band { position: absolute; left: 0; top: 1064px; width: 506px; height: 136px; background: var(--teal); }
  .visit-intro { position: absolute; left: 40px; top: 1074px; font-size: 16.5px; line-height: 23px; color: var(--night); white-space: nowrap; }
  .visit-cta { position: absolute; left: 40px; top: 1118px; font-size: 21px; line-height: 28px; font-weight: 700; color: var(--night); }
  .visit-web { position: absolute; left: 40px; top: 1153px; display: flex; align-items: center; gap: 9px; font-size: 20px; line-height: 26px; font-style: italic; color: var(--night); white-space: nowrap; }
  .projects-intro { position: absolute; left: 549px; top: 641px; font-size: 21.5px; line-height: 30px; color: var(--white); white-space: nowrap; }
  .projects-intro strong { font-weight: 700; }
  .projects-rule { position: absolute; left: 549px; top: 706px; width: 81px; height: 2px; background: var(--white); }
  .project-list { position: absolute; left: 546px; top: 745px; list-style: none; color: var(--white); font-size: 18.5px; white-space: nowrap; }
  .project-list li { display: flex; align-items: center; gap: 18px; height: 40.7px; }
  .project-list li.more { padding-left: 44px; }
  .project-list svg { flex: none; }
  .social-box {
    position: absolute; left: 486px; top: 1109px; width: 470px; height: 62px;
    background: var(--social-box); color: var(--white); white-space: nowrap;
  }
  .social-box .mark { position: absolute; left: 18px; top: 16px; width: 30px; height: 30px; background: var(--white); opacity: 0.9; }
  .social-box .lead { position: absolute; left: 72px; top: 11px; font-size: 14px; line-height: 19px; font-weight: 700; }
  .social-box .url { position: absolute; left: 72px; top: 31px; font-size: 15px; line-height: 20px; font-style: italic; }
  .social-notch { position: absolute; left: 486px; top: 1100px; width: 20px; height: 9px; }
</style>
</head>
<body>
<div class="flyer">
  <div class="hero-photo" role="img" aria-label="Photo of three laughing men with arms around each other outdoors in front of green trees"></div>

  <svg class="header-art" viewBox="0 0 1000 130" aria-hidden="true">
    <polygon points="0,0 1000,0 1000,52 482,52 440,110 0,110" fill="#141414"/>
    <polygon points="482,52 1000,52 1000,63 474,63" fill="#00a990"/>
    <polygon points="0,110 440,110 429,125 0,125" fill="#00a990"/>
  </svg>
  <div class="brand-name">HARBOUR FELLOWS</div>

  <h1 class="headline">Social. Support. Mateship. Community.</h1>
  <div class="headline-rule"></div>

  <div class="projects-panel"></div>

  <p class="about"><strong>Harbour Fellows Inc.</strong> is a community group<br>that supports the positive activity, engagement<br>and inclusion of men in Melbourne’s<br>Dandenong Ranges. &nbsp;Our aim is to reduce the<br>number of men who are socially<br>disadvantaged, marginalised or isolated to<br>become productive, active members of the<br>local community. &nbsp;We do this by providing<br>opportunities for men (18 years+) to come<br>together in open, non-judgemental, safe<br>spaces and participate in a range of social<br>activities that encourage new friendships,<br>normalise help-seeking behaviours and link<br>with local support services.</p>

  <svg class="divider-strip" viewBox="0 0 350 10" aria-hidden="true">
    <polygon points="0,0 340,0 350,10 0,10" fill="#00705f"/>
  </svg>
  <div class="visit-band"></div>
  <p class="visit-intro">For a list of our current activities<br>and to find our how you can get involved,</p>
  <p class="visit-cta">please visit us online at:</p>
  <p class="visit-web">
    <svg width="22" height="22" viewBox="0 0 22 22" aria-hidden="true" fill="none" stroke="#0b0b26" stroke-width="1.3">
      <circle cx="11" cy="11" r="9.5"/><ellipse cx="11" cy="11" rx="4.5" ry="9.5"/>
      <line x1="1.5" y1="11" x2="20.5" y2="11"/><line x1="3" y1="6.5" x2="19" y2="6.5"/><line x1="3" y1="15.5" x2="19" y2="15.5"/>
    </svg>
    www.harbourfellows.org.au
  </p>

  <p class="projects-intro">We run a number of projects each year,<br><strong>which currently include:</strong></p>
  <div class="projects-rule"></div>
  <ul class="project-list">
    <li><svg width="26" height="26" viewBox="0 0 26 26" aria-hidden="true"><circle cx="13" cy="13" r="12" fill="#00a990"/><polyline points="7,13.5 11.5,18 19,9" fill="none" stroke="#fff" stroke-width="3" stroke-linecap="round" stroke-linejoin="round"/></svg>Dads and kids playgroup;</li>
    <li><svg width="26" height="26" viewBox="0 0 26 26" aria-hidden="true"><circle cx="13" cy="13" r="12" fill="#00a990"/><polyline points="7,13.5 11.5,18 19,9" fill="none" stroke="#fff" stroke-width="3" stroke-linecap="round" stroke-linejoin="round"/></svg>Games Night;</li>
    <li><svg width="26" height="26" viewBox="0 0 26 26" aria-hidden="true"><circle cx="13" cy="13" r="12" fill="#00a990"/><polyline points="7,13.5 11.5,18 19,9" fill="none" stroke="#fff" stroke-width="3" stroke-linecap="round" stroke-linejoin="round"/></svg>Yarning Circle (men’s discussion group);</li>
    <li><svg width="26" height="26" viewBox="0 0 26 26" aria-hidden="true"><circle cx="13" cy="13" r="12" fill="#00a990"/><polyline points="7,13.5 11.5,18 19,9" fill="none" stroke="#fff" stroke-width="3" stroke-linecap="round" stroke-linejoin="round"/></svg>GBTIQ+ social dinners;</li>
    <li><svg width="26" height="26" viewBox="0 0 26 26" aria-hidden="true"><circle cx="13" cy="13" r="12" fill="#00a990"/><polyline points="7,13.5 11.5,18 19,9" fill="none" stroke="#fff" stroke-width="3" stroke-linecap="round" stroke-linejoin="round"/></svg>Shared Services working bee’s;</li>
    <li><svg width="26" height="26" viewBox="0 0 26 26" aria-hidden="true"><circle cx="13" cy="13" r="12" fill="#00a990"/><polyline points="7,13.5 11.5,18 19,9" fill="none" stroke="#fff" stroke-width="3" stroke-linecap="round" stroke-linejoin="round"/></svg>Guest speakers;</li>
    <li><svg width="26" height="26" viewBox="0 0 26 26" aria-hidden="true"><circle cx="13" cy="13" r="12" fill="#00a990"/><polyline points="7,13.5 11.5,18 19,9" fill="none" stroke="#fff" stroke-width="3" stroke-linecap="round" stroke-linejoin="round"/></svg>Annual men’s gathering</li>
    <li class="more">And More...</li>
  </ul>

  <svg class="social-notch" viewBox="0 0 20 9" aria-hidden="true"><polygon points="0,9 20,0 20,9" fill="#0b0b26"/></svg>
  <div class="social-box">
    <span class="mark" aria-hidden="true"></span>
    <span class="lead">join our Fellows Connect page for our latest updates:</span>
    <span class="url">www.fellowsconnect.com/harbourfellowsAU/</span>
  </div>
</div>
</body>
</html>
```